Zielgruppe
Seminare
Aufgabenstellung
Bitte wie das beigefügte Beispiel. Sehr gerne mit runden Übergang zum nächsten Thema. Am Ende den Text: Brenntaler Fachakademie Oststeig ... mit Logo.
Hier die Vorgaben des Banner-Hersteller:
Datenformat (inkl. 10 mm Beschnitt): 102 x 227 cm
Endformat: 100 x 200 cm
Sichtbarer Bereich: 100 x 200 cm
Bedruckbarer Bereich: 100 x 225 cm
Auflösung: 150 dpi
umlaufend 10 mm Beschnitt anlegen, wichtige Informationen mit mind. 10 mm Abstand zum Endformat
Schriften müssen vollständig eingebettet oder in Kurven konvertiert werden
Farbmodus: CMYK, FOGRA51 (PSO Coated v3)
Farbauftrag: maximal 300 %

```html
<!DOCTYPE html>
<html lang="de">
<head>
<meta charset="utf-8">
<title>Stress – Seminarbanner</title>
<link rel="stylesheet" href="https://fonts.googleapis.com/css2?family=Open+Sans:wght@400;600;700&display=swap">
<style>
  :root {
    --rust: #9c3a12;
    --tan: #c98a55;
    --olive: #5c6455;
    --cream: #f1e6de;
    --ink: #111111;
    --white: #ffffff;
    --gold: #d9b44a;
    --photo-warm-a: #ece8e4;
    --photo-warm-b: #b59c88;
    --photo-skin-a: #f2efec;
    --photo-skin-b: #b9a08d;
    --photo-mono-a: #d6d6d6;
    --photo-mono-b: #4a4a4a;
  }
  html, body {
    margin: 0;
    padding: 0;
    width: 1200px;
    height: 2673px;
    overflow: hidden;
    background: var(--cream);
  }
  .banner {
    position: relative;
    width: 1200px;
    height: 2673px;
    font-family: "Open Sans", Arial, sans-serif;
    overflow: hidden;
  }
  .backdrop { position: absolute; inset: 0; }
  .photo {
    position: absolute;
    border-radius: 50%;
  }
  .photo--stopwatch {
    left: -310px; top: -10px; width: 700px; height: 700px;
    background: radial-gradient(circle at 62% 48%, var(--photo-warm-a) 0 38%, var(--photo-warm-b) 100%);
  }
  .photo--frustrated {
    left: 674px; top: 767px; width: 686px; height: 686px;
    background: radial-gradient(circle at 45% 45%, var(--photo-skin-b) 0 30%, var(--photo-skin-a) 70%);
  }
  .photo--despair {
    left: -255px; top: 1699px; width: 690px; height: 690px;
    background: linear-gradient(180deg, var(--photo-mono-a) 0%, #9a9a9a 45%, var(--photo-mono-b) 100%);
  }
  .block { position: absolute; }
  .block h2 {
    margin: 0;
    font-weight: 700;
    letter-spacing: 2px;
    line-height: 1.05;
    white-space: nowrap;
  }
  .block ul { list-style: none; margin: 0; padding: 0; }
  .block li {
    position: relative;
    padding-left: 38px;
    font-size: 26px;
    white-space: nowrap;
  }
  .block li::before {
    content: "";
    position: absolute;
    left: 0; top: 50%;
    margin-top: -6px;
    border-left: 9px solid currentColor;
    border-top: 6px solid transparent;
    border-bottom: 6px solid transparent;
  }
  .block--stressors {
    left: 440px; top: 122px; color: var(--white);
    transform: rotate(-4deg); transform-origin: left top;
  }
  .block--stressors h2 { font-size: 56px; margin-bottom: 14px; }
  .block--stressors li { line-height: 44px; font-size: 27px; }
  .block--amplifiers {
    left: 44px; top: 990px; color: var(--ink);
    transform: rotate(-3deg); transform-origin: left top;
  }
  .block--amplifiers h2 { font-size: 56px; margin-bottom: 18px; }
  .block--amplifiers li { line-height: 40px; }
  .block--reaction {
    left: 536px; top: 1780px; color: var(--white);
    transform: rotate(2deg); transform-origin: left top;
  }
  .block--reaction h2 { font-size: 58px; margin-bottom: 14px; }
  .block--reaction li { line-height: 39px; }
  .brand {
    position: absolute;
    right: 418px; top: 2424px;
    text-align: right;
    font-size: 32px;
    font-weight: 600;
    line-height: 47px;
    letter-spacing: 1px;
    color: var(--ink);
  }
  .brand-mark {
    position: absolute;
    left: 841px; top: 2354px;
    width: 272px; height: 272px;
    border-radius: 50%;
    background: var(--gold);
  }
</style>
</head>
<body>
<div class="banner">
  <svg class="backdrop" width="1200" height="2673" viewBox="0 0 1200 2673">
    <rect width="1200" height="2673" fill="var(--cream)"/>
    <path class="band band--rust" d="M0 0 H1200 V630 Q500 560 0 880 Z" fill="var(--rust)"/>
    <path class="band band--tan" d="M0 930 Q500 630 1200 745 V1490 Q500 1440 0 1635 Z" fill="var(--tan)"/>
    <path class="band band--olive" d="M0 1665 Q500 1490 1200 1595 V2220 Q600 2200 0 2400 Z" fill="var(--olive)"/>
  </svg>

  <div class="photo photo--stopwatch" role="img" aria-label="Hand hält eine Stoppuhr"></div>
  <div class="photo photo--frustrated" role="img" aria-label="Gestresster Mann, dem Dampf aus den Ohren steigt"></div>
  <div class="photo photo--despair" role="img" aria-label="Verzweifelter Mann im Anzug sitzt im hohen Gras, Schwarzweiß"></div>

  <section class="block block--stressors">
    <h2>STRESSOREN</h2>
    <ul>
      <li>Verlust des Arbeitsplatzes</li>
      <li>Zeitdruck, Termindruck, Stau</li>
      <li>Soziale Konflikte/Trennung/Scheidung</li>
      <li>Ständiger Lärm</li>
      <li>Informationsüberflutung</li>
      <li>Hohe Leistungsanforderungen</li>
      <li>Falsche oder schlechte Ernährung</li>
      <li>Falsche oder schlechte Lebensweise</li>
      <li>uvm.</li>
    </ul>
  </section>

  <section class="block block--amplifiers">
    <h2>PERSÖNLICHE<br>STRESSVERSTÄRKER</h2>
    <ul>
      <li>Selbstüberforderung</li>
      <li>Negative Gedanken</li>
      <li>Es allen recht machen wollen</li>
      <li>Nicht Nein-Sagen können</li>
      <li>Ungeduld</li>
      <li>uvm.</li>
    </ul>
  </section>

  <section class="block block--reaction">
    <h2>STRESSREAKTION</h2>
    <ul>
      <li>Konzentrationsstörungen</li>
      <li>Aggressivität, Gereiztheit</li>
      <li>Angst</li>
      <li>Infektanfälligkeit</li>
      <li>Schlafstörungen</li>
      <li>Erschöpfungssyndrom</li>
      <li>Krankheiten</li>
      <li>uvm.</li>
    </ul>
  </section>

  <div class="brand">BRENNTALER<br>FACHAKADEMIE<br>OSTSTEIG</div>
  <div class="brand-mark" aria-hidden="true"></div>
</div>
</body>
</html>
```